Have Logo - Need Business Card Design!!!

I am looking for a business card design for a real estate development business. The company name is Calder Crest Property Group. I already have a logo created by Sketch Harbor and would like this logo to be incorporated into the design. I have uploaded the files. The card needs to be professional, but visually interesting. Not necessary to be double-sided, but if you want to get creative and can think of something to put on the back then have at it.

Target Market(s)

The target audience for these business cards will be professionals in the real estate industry.

Industry/Entity Type

Real Estate

Requirements
Must have
• The business card must have all the necessary items for a business card, i.e. company name, our logo, name (however, not title necessary), office address, office phone number, cell number, fax number, website address, etc.

You can use the information below for the card:

Gregory L. Hanlon
782 Marlowe Avenue
San Francisco, California 94127

www.mvrealtypartners.example
ghanlon@mvrealtypartners.example
Office: 415-555-0142
Fax: 415-555-0143
Cell: 415-555-0186

```html
<!DOCTYPE html>
<html lang="en">
<head>
<meta charset="utf-8">
<title>Calder Crest Property Group — Business Card</title>
<link rel="stylesheet" href="https://fonts.googleapis.com/css2?family=Source+Sans+3:ital,wght@0,400;0,600;1,700&display=swap">
<style>
  :root {
    --backdrop: #d9dadc;
    --paper: #ffffff;
    --navy: #1f3a6e;
    --green: #0b8a3e;
    --contact-ink: #e3e8f2;
    --name-ink: #ffffff;
  }
  * { margin: 0; padding: 0; box-sizing: border-box; }
  html, body {
    width: 1200px;
    height: 800px;
    overflow: hidden;
    background: var(--backdrop);
    font-family: "Source Sans 3", "Segoe UI", sans-serif;
  }
  .canvas {
    position: relative;
    width: 1200px;
    height: 800px;
    display: flex;
    align-items: center;
    justify-content: center;
  }
  .business-card {
    position: relative;
    width: 980px;
    height: 560px;
    background: var(--paper);
    box-shadow: 0 10px 28px rgba(0, 0, 0, 0.25);
    overflow: hidden;
  }
  .card-bands {
    position: absolute;
    inset: 0;
    width: 100%;
    height: 100%;
  }
  .band-green { fill: var(--green); }
  .band-navy { fill: var(--navy); }

  .company-name {
    position: absolute;
    top: 82px;
    right: 64px;
    font-size: 42px;
    font-weight: 600;
    color: var(--green);
    letter-spacing: 0.5px;
    line-height: 1;
  }

  .holder {
    position: absolute;
    left: 52px;
    top: 372px;
  }
  .holder__name {
    font-size: 42px;
    font-weight: 700;
    font-style: italic;
    color: var(--name-ink);
    line-height: 1.05;
  }
  .holder__title {
    font-size: 30px;
    font-weight: 400;
    color: var(--green);
    line-height: 1.1;
  }

  .website {
    position: absolute;
    left: 52px;
    bottom: 36px;
    font-size: 22px;
    font-weight: 400;
    color: var(--name-ink);
  }

  .contact-list {
    position: absolute;
    right: 52px;
    top: 344px;
    list-style: none;
    text-align: right;
    font-size: 22px;
    line-height: 1.32;
    color: var(--contact-ink);
  }
</style>
</head>
<body>
<main class="canvas">
  <article class="business-card">
    <svg class="card-bands" viewBox="0 0 980 560" preserveAspectRatio="none" aria-hidden="true">
      <path class="band-green" d="M0 318 Q 490 296 980 258 L 980 290 Q 490 314 0 322 Z"/>
      <path class="band-navy" d="M0 322 Q 490 314 980 290 L 980 560 L 0 560 Z"/>
    </svg>

    <header class="company-name">Calder Crest Property Group</header>

    <section class="holder">
      <h1 class="holder__name">Gregory L. Hanlon</h1>
      <p class="holder__title">CEO</p>
    </section>

    <p class="website">www.caldercrest.example</p>

    <ul class="contact-list">
      <li>782 Marlowe Avenue</li>
      <li>San Francisco, CA 94127</li>
      <li>(415) 555-0142</li>
      <li>Fax (415) 555-0143</li>
      <li>Cell (415) 555-0186</li>
      <li>ghanlon@caldercrest.example</li>
    </ul>
  </article>
</main>
</body>
</html>
```